stationary for a modern hotel
Venmiro Hotels
Project: stationary for a modern hotel
stationary for a modern hotel - Hospitality Industry
Creative Brief
Use same font as used in my logo
anything that can go very well with my logo
Simple
Tundeyemi Okafordike
G.M
Venmiro Hotels Plot 318,Adebanjo-Ekwueme Way,Garki District Abuja Nigeria
tunde@venmirohotels.com
www.venmirohotels.com

```html
<!DOCTYPE html>
<html lang="en">
<head>
<meta charset="utf-8">
<title>Venmiro Hotels – Business Cards</title>
<link href="https://fonts.googleapis.com/css2?family=Arimo:wght@400;700&display=swap" rel="stylesheet">
<style>
  :root {
    --frame: #2a2a2a;
    --backdrop: #c9c9c9;
    --card-white: #ffffff;
    --tan: #a67d57;
    --brown-dark: #5a3818;
    --brown-text: #a07648;
    --ink: #2b2b2b;
    --card-edge: #9a9a9a;
  }
  * { margin: 0; padding: 0; box-sizing: border-box; }
  html, body { width: 1200px; height: 703px; overflow: hidden; background: var(--frame); }
  .canvas {
    position: relative;
    width: 1200px; height: 703px;
    background: var(--backdrop);
    border: 10px solid var(--frame);
    font-family: "Arimo", Arial, sans-serif;
  }
  .card {
    position: absolute;
    width: 494px; height: 283px;
    border-radius: 22px;
    overflow: hidden;
    border: 1px solid var(--card-edge);
  }
  .card--front { left: 86px; top: 43px; background: var(--card-white); }
  .card--tan   { left: 595px; top: 43px; background: var(--tan); }
  .card--white { left: 86px; top: 343px; background: var(--card-white); }
  .card--dark  { left: 595px; top: 343px; background: var(--brown-dark); }

  .card__swoosh { position: absolute; inset: 0; width: 100%; height: 100%; }

  .brand {
    position: absolute;
    font-weight: 400;
    letter-spacing: 3px;
    text-transform: uppercase;
    white-space: nowrap;
  }
  .card--front .brand { left: 14px; top: 78px; font-size: 17px; color: var(--tan); }
  .brand--center {
    left: 0; right: 0; top: 50%;
    transform: translateY(-50%);
    text-align: center;
    font-size: 30px;
  }
  .card--tan .brand, .card--dark .brand { color: #ffffff; }
  .card--white .brand { color: var(--tan); }

  .person { position: absolute; left: 0; width: 494px; top: 128px; text-align: center; }
  .person__name { font-size: 26px; font-weight: 700; color: var(--brown-text); padding-left: 20px; }
  .person__role { font-size: 14px; color: var(--ink); margin-top: 4px; padding-left: 20px; }

  .contact {
    position: absolute; left: 20px; top: 217px;
    font-size: 12.5px; line-height: 15px; color: var(--ink);
  }
  .contact__label { color: var(--tan); }
  .contact__web { color: var(--tan); }
</style>
</head>
<body>
<div class="canvas">

  <section class="card card--front">
    <svg class="card__swoosh" viewBox="0 0 494 283" aria-hidden="true">
      <path d="M0 0 H494 V0 Z" fill="none"/>
      <path d="M95 0 H494 V20 C420 22 380 40 340 52 C260 72 180 52 95 0 Z" fill="var(--tan)"/>
      <path d="M400 0 H494 V62 C470 40 440 22 400 0 Z" fill="var(--brown-dark)"/>
      <path d="M380 0 C400 20 430 32 400 62 C430 48 470 50 494 62 V0 Z" fill="var(--brown-dark)" opacity="0.85"/>
    </svg>
    <div class="brand">Venmiro Hotels</div>
    <div class="person">
      <div class="person__name">Tundeyemi Okafordike</div>
      <div class="person__role">G.M</div>
    </div>
    <div class="contact">
      <div>Venmiro Hotels, Plot 318,Adebanjo-Ekwueme Way</div>
      <div>Garki District, Abuja, Nigeria</div>
      <div><span class="contact__label">Cell:</span> +234 803 555 0142 | <span class="contact__label">Phone:</span> +234 809 555 0187</div>
      <div><span class="contact__label">Email:</span> tunde@venmirohotels.com | <span class="contact__web">www.venmirohotels.com</span></div>
    </div>
  </section>

  <section class="card card--tan">
    <div class="brand brand--center">Venmiro Hotels</div>
  </section>

  <section class="card card--white">
    <div class="brand brand--center">Venmiro Hotels</div>
  </section>

  <section class="card card--dark">
    <div class="brand brand--center">Venmiro Hotels</div>
  </section>

</div>
</body>
</html>
```